Business Card for Web Design consulting firm

Business card designs for Web Design consulting firm

Target Market(s)

English speaking adults ages 30 - 60. Predominantly professional services eg. Doctor, Dentist

Industry/Entity Type

Consulting

Requirements
Must have
• Double sided card

```html
<!DOCTYPE html>
<html lang="en">
<head>
<meta charset="utf-8">
<title>Lumeno Business Card</title>
<link rel="stylesheet" href="https://fonts.googleapis.com/css2?family=Marcellus+SC&display=swap">
<style>
  :root {
    --orange: #f49b22;
    --charcoal: #4a4a4a;
    --ink: #222222;
    --paper: #ffffff;
    --edge: #e4e4e4;
  }
  * { margin: 0; padding: 0; box-sizing: border-box; }
  html, body {
    width: 1050px;
    height: 1200px;
    overflow: hidden;
    background: var(--paper);
  }
  body {
    position: relative;
    font-family: "Marcellus SC", serif;
    color: var(--ink);
  }
  .card {
    position: absolute;
    left: 22px;
    width: 1006px;
    height: 565px;
    background: var(--paper);
    border: 1px solid var(--edge);
    box-shadow: 1px 2px 4px rgba(0,0,0,0.18);
    overflow: hidden;
  }
  .card--front { top: 18px; }
  .card--back { top: 618px; }

  .identity {
    position: absolute;
    right: 54px;
    top: 32px;
    text-align: right;
  }
  .identity__name {
    color: var(--orange);
    font-size: 30px;
    letter-spacing: 1.5px;
    line-height: 33px;
  }
  .identity__role {
    color: var(--ink);
    font-size: 30px;
    letter-spacing: 1.5px;
    line-height: 33px;
  }

  .address {
    position: absolute;
    right: 54px;
    top: 150px;
    text-align: right;
    font-size: 22px;
    line-height: 24px;
    letter-spacing: 1px;
  }

  .contacts {
    position: absolute;
    right: 54px;
    top: 243px;
    text-align: right;
    font-size: 22px;
    line-height: 24px;
    letter-spacing: 1px;
    list-style: none;
  }
  .contacts__label {
    color: var(--orange);
    margin-right: 16px;
  }

  .brand {
    position: absolute;
    left: 30px;
    top: 470px;
    display: flex;
    align-items: center;
    gap: 22px;
  }
  .brand__dot {
    width: 34px;
    height: 34px;
    border-radius: 50%;
    background: var(--orange);
  }
  .brand__name {
    color: var(--charcoal);
    font-size: 66px;
    letter-spacing: 10px;
    line-height: 1;
  }

  .brand--back {
    left: 0;
    right: 0;
    top: 0;
    bottom: 0;
    justify-content: center;
    gap: 40px;
  }
  .brand--back .brand__dot {
    width: 90px;
    height: 90px;
  }
  .brand--back .brand__name {
    font-size: 150px;
    letter-spacing: 18px;
  }
</style>
</head>
<body>
  <section class="card card--front" aria-label="Card front">
    <header class="identity">
      <p class="identity__name">Daniel Carter</p>
      <p class="identity__role">Sales Person</p>
    </header>
    <address class="address" style="font-style: normal;">
      <p>22 Sample Lane</p>
      <p>Harbourton, 4100</p>
    </address>
    <ul class="contacts">
      <li><span class="contacts__label">P</span>07 55501234</li>
      <li><span class="contacts__label">M</span>0455501234</li>
      <li><span class="contacts__label">E</span>info@lumeno.com</li>
      <li><span class="contacts__label">W</span>www.lumeno.com</li>
    </ul>
    <div class="brand">
      <span class="brand__dot" aria-hidden="true"></span>
      <span class="brand__name">Lumeno</span>
    </div>
  </section>

  <section class="card card--back" aria-label="Card back">
    <div class="brand brand--back">
      <span class="brand__dot" aria-hidden="true"></span>
      <span class="brand__name">Lumeno</span>
    </div>
  </section>
</body>
</html>
```